Consulting firm need a professional powerpoint design

A startup Climate change firm needs a powerpoint template design. The design should reflect aspects of climate change adaptation, resilience and environmental sustainability.

The powerpoint design must convey aspects of nature and climate action for a resilient society.

The last slide of the powerpoint must have a allocation for a slogan such as 'Linking science and decision-making'.

Use the colors in the logo and business card for the powerpoint design.

Target Market(s)

Government and industry

Font styles to use
Sans Serif
Other font styles liked:
• nexa font family

Colors
85cae6
abd037
fece3e

Requirements
Must have
• - Colors used in logo and business card
- Convey science and nature
- Professional
Nice to have
• Many pages
Should not have
• Not complicated

```html
<!DOCTYPE html>
<html lang="en">
<head>
<meta charset="utf-8">
<title>Terravane Presentation Deck</title>
<link href="https://fonts.googleapis.com/css2?family=Montserrat:wght@400;500;600;700;800&family=Poppins:wght@300;400;500&display=swap" rel="stylesheet">
<style>
:root{
  --navy:#1f3558;
  --navy-dark:#16284a;
  --green:#7cc242;
  --lime:#abd037;
  --yellow:#fece3e;
  --orange:#f6a01a;
  --sky:#85cae6;
  --blue:#2aa6dc;
  --ink:#2b2b2b;
  --muted:#7a7f88;
  --paper:#ffffff;
  --stage:#eceff4;
  --hero-blue:#5a66b3;
}
*{margin:0;padding:0;box-sizing:border-box}
html,body{width:1200px;height:2563px;overflow:hidden}
body{background:var(--paper);font-family:"Montserrat",sans-serif;color:var(--ink);position:relative}

/* hero */
.hero{position:absolute;left:0;top:0;width:1200px;height:500px;background:linear-gradient(160deg,#dfe4ec 0%,#eef1f5 60%,#f6f7f9 100%)}
.hero-title{position:absolute;left:70px;top:182px;line-height:1}
.hero-title b{display:block;font-weight:800;font-size:62px;color:var(--hero-blue);letter-spacing:-.5px}
.hero-title span{display:block;font-weight:400;font-size:60px;color:#1c1c1c;margin:4px 0 0 128px}

/* slide base */
.slide{position:absolute;width:387px;height:217px;background:var(--paper);overflow:hidden;box-shadow:0 0 0 1px #e3e6eb}
.c1{left:15px}.c2{left:410px}.c3{left:804px}
.hero-slide{left:566px;top:86px;width:470px;height:264px}
.ph{position:absolute}

.bar{position:absolute;left:0;top:0;width:100%;height:27px;background:var(--navy)}
.bar::after{content:"";position:absolute;right:0;top:0;width:92px;height:27px;background:var(--paper);clip-path:polygon(14% 0,100% 0,100% 100%,0 100%)}
.bar::before{content:"";position:absolute;left:0;bottom:-2px;width:100%;height:2px;background:linear-gradient(90deg,var(--navy) 0 70%,var(--lime) 70% 80%,var(--yellow) 80% 90%,var(--blue) 90%)}
.bar-title{position:absolute;left:7px;top:5px;color:#fff;font-weight:700;font-size:8.5px;letter-spacing:-.1px;line-height:1}
.bar-title small{display:block;font-size:4px;font-weight:800;letter-spacing:1px;color:var(--yellow);margin-top:1px}
.brand{position:absolute;right:9px;top:9px;z-index:2;display:flex;align-items:center;gap:3px;font-weight:700;font-size:6.5px;color:var(--navy);letter-spacing:.3px}
.brand i{width:8px;height:8px;border-radius:50%;background:var(--green);display:block}

.foot{position:absolute;left:0;bottom:0;width:100%;height:7px;background:linear-gradient(90deg,var(--navy) 0 60%,var(--lime) 60% 73%,var(--yellow) 73% 86%,var(--blue) 86%)}
.foot span{position:absolute;left:10px;top:1.5px;font-size:3.4px;color:#fff;font-family:"Poppins",sans-serif}

.tiny{font-family:"Poppins",sans-serif;font-size:3.6px;line-height:1.45;color:var(--muted)}
.h6{font-weight:700;font-size:5px;color:var(--navy)}

/* cover */
.cover-brand{display:flex;align-items:center;gap:4px;font-weight:700;color:var(--navy);letter-spacing:.5px}
.cover-brand i{border-radius:50%;background:var(--green);display:block}
.cover-t1{font-weight:600;color:var(--navy);line-height:1}
.cover-t2{font-weight:400;color:var(--navy);letter-spacing:2px;line-height:1}
.cover-sub{font-weight:500;color:var(--navy);letter-spacing:2px}

.toc li{list-style:none;font-family:"Poppins",sans-serif;font-size:5px;color:#888;display:flex;gap:16px;height:15.5px}
.toc li em{font-style:normal;width:6px}

.pill{position:absolute;background:var(--navy);color:#fff;border-radius:8px;font-weight:700;font-size:6px;text-align:center;display:flex;align-items:center;justify-content:center;padding:0 12px;line-height:1.35}

.icon-dot{width:16px;height:16px;border-radius:50%;background:var(--green);border:2px solid #d9ecc5}
.num{width:13px;height:13px;border-radius:50%;display:flex;align-items:center;justify-content:center;color:#fff;font-size:4.5px;font-weight:700}

.card{position:absolute;top:45px;width:88px;height:140px;border-radius:8px;color:#fff;text-align:center}
.card .disc{width:44px;height:44px;border-radius:50%;background:#fff;margin:14px auto 24px;display:flex;align-items:center;justify-content:center}
.card b{font-size:5px;font-weight:600;display:block;margin-bottom:5px}
.card p{font-family:"Poppins",sans-serif;font-size:3.5px;line-height:1.5;padding:0 8px}

.info-box{position:absolute;width:64px;height:18px;border-radius:2px;color:#fff;font-size:3.2px;display:flex;align-items:center;justify-content:center;text-align:center;padding:0 4px}

.team-card{position:absolute;top:50px;width:84px;height:135px}
.team-card .avatar{width:34px;height:34px;border-radius:50%;background:linear-gradient(160deg,#9aa3ad,#4b5563)}
.team-card b{display:block;font-size:5.2px;font-weight:600;color:var(--navy);margin-top:6px}
.team-card span{display:block;font-size:5px;color:var(--muted);margin-bottom:5px}
.team-card .line{position:absolute;bottom:0;left:0;width:100%;height:2px;background:var(--green)}

.label{width:62px;height:15px;color:#fff;font-size:3.6px;font-weight:600;display:flex;align-items:center;justify-content:center}

.grid-table{position:absolute;border-collapse:collapse;font-size:3.4px;color:#555;text-align:center}
.grid-table td,.grid-table th{border-bottom:.5px solid #d5d9df;height:9px}
.grid-table th{color:var(--navy);font-weight:700;border-bottom:1.5px solid var(--navy)}

.step{position:absolute;background:var(--navy);color:#fff;font-size:4.5px;font-weight:700;text-align:right;padding:2px 4px;height:10px;width:48px}

.overlay-title{position:absolute;color:#fff;font-weight:600}
</style>
</head>
<body>

<!-- hero -->
<section class="hero">
  <h1 class="hero-title"><b>Presentation</b><span>Deck</span></h1>

  <div class="slide hero-slide">
    <div class="ph" role="img" aria-label="Photo of a climate protester holding a hand-made planet sign" style="left:0;top:0;width:230px;height:264px;background:linear-gradient(110deg,#c9d3cf 0%,#e4e2d8 55%,#ffffff 100%)"></div>
    <div class="cover-brand" style="position:absolute;left:232px;top:84px;font-size:12px"><i style="width:16px;height:16px"></i>TERRAVANE</div>
    <div class="tiny" style="position:absolute;left:266px;top:100px;font-size:4px">Linking science and decision-making</div>
    <div class="cover-t1" style="position:absolute;left:232px;top:128px;font-size:16px">ADD YOUR AWESOME</div>
    <div class="cover-t2" style="position:absolute;left:232px;top:146px;font-size:27px">TITLE HERE</div>
    <div class="cover-sub" style="position:absolute;left:234px;top:178px;font-size:7px">HERE ADD YOUR SUBTITLE</div>
    <div class="cover-sub" style="position:absolute;left:240px;top:234px;font-size:8px">2020</div>
  </div>
</section>

<!-- row 1 -->
<div class="slide c1" style="top:500px">
  <div class="ph" role="img" aria-label="Photo of a climate protester holding a hand-made planet sign" style="left:0;top:0;width:190px;height:217px;background:linear-gradient(110deg,#c9d3cf 0%,#e4e2d8 55%,#ffffff 100%)"></div>
  <div class="cover-brand" style="position:absolute;left:190px;top:68px;font-size:10px"><i style="width:13px;height:13px"></i>TERRAVANE</div>
  <div class="cover-t1" style="position:absolute;left:191px;top:104px;font-size:14px">ADD YOUR AWESOME</div>
  <div class="cover-t2" style="position:absolute;left:191px;top:119px;font-size:23px">TITLE HERE</div>
  <div class="cover-sub" style="position:absolute;left:192px;top:145px;font-size:6px">HERE ADD YOUR SUBTITLE</div>
  <div class="cover-sub" style="position:absolute;left:196px;top:191px;font-size:6.5px">2020</div>
</div>

<div class="slide c2" style="top:500px">
  <div class="ph" role="img" aria-label="Photo of a wind turbine at dusk under a navy overlay" style="inset:0;background:linear-gradient(180deg,#2c4468 0%,#23395c 60%,#1c2f4f 100%)"></div>
  <div class="cover-brand" style="position:absolute;left:136px;top:60px;font-size:10px;color:#fff"><i style="width:13px;height:13px"></i>TERRAVANE</div>
  <div class="cover-t1" style="position:absolute;left:0;width:100%;text-align:center;top:99px;font-size:13px;color:#fff">ADD YOUR AWESOME</div>
  <div class="cover-t2" style="position:absolute;left:0;width:100%;text-align:center;top:113px;font-size:23px;color:#fff">TITLE HERE</div>
  <div class="cover-sub" style="position:absolute;left:0;width:100%;text-align:center;top:139px;font-size:6px;color:#fff">HERE ADD YOUR SUBTITLE</div>
  <div class="cover-sub" style="position:absolute;left:0;width:100%;text-align:center;top:204px;font-size:5px;color:#fff">2020</div>
</div>

<div class="slide c3" style="top:500px">
  <div class="ph" role="img" aria-label="Photo of hands holding a glowing light bulb" style="left:0;top:0;width:120px;height:217px;background:radial-gradient(circle at 55% 55%,#d9812e 0%,#7a3d16 35%,#1e1410 75%)"></div>
  <div style="position:absolute;left:120px;top:0;width:25px;height:217px;background:var(--navy)"></div>
  <div style="position:absolute;left:123px;top:186px;transform:rotate(-90deg);transform-origin:0 0;color:#fff;font-weight:700;font-size:10px;white-space:nowrap">TABLE OF CONTENTS</div>
  <ul class="toc" style="position:absolute;left:232px;top:37px">
    <li><em>i</em>Introduction</li><li><em>ii</em>About Us</li><li><em>iii</em>Welcome Message</li><li><em>iv</em>Company Profile</li><li><em>v</em>Team</li><li><em>vi</em>Team Group</li><li><em>vii</em>Portfolio</li><li><em>viii</em>Info graphic</li><li><em>ix</em>Contact Us</li><li><em>x</em>Data Chart</li>
  </ul>
</div>

<!-- row 2 -->
<div class="slide c1" style="top:731px">
  <div class="bar"></div><span class="brand"><i></i>TERRAVANE</span>
  <div class="h6" style="position:absolute;left:18px;top:55px;font-size:5px">Lorem ipsum dolor sit amet, consectetur adipiscing elit.</div>
  <p class="tiny" style="position:absolute;left:18px;top:76px;width:352px;color:#555">Fusce sit amet neque sodales, faucibus ex eu, efficitur lacus. Cras imperdiet, nulla nec sagittis pulvinar, neque augue iaculis risus, ac fringilla felis urna fermentum mi. Ut vehicula vel enim sit amet vulputate. Aenean malesuada consectetur diam, ac convallis quam tincidunt eget. Nam vitae elementum ipsum. Proin vitae blandit enim. Donec congue convallis commodo. Aenean vel lacus. Sed in est ultrices dolor faucibus feugiat. Nullam cursus sollicitudin dictum. Donec a ex at enim consectetur auctor. Aliquam ut laoreet neque. In viverra nunc purus sodales diam. Sed ullamcorper at ante eget euismod. Cras nec dui at tellus ut odio fermentum.</p>
  <p class="tiny" style="position:absolute;left:18px;top:152px;width:352px;color:#555">Maecenas in purus et tellus tincidunt sodales eu sed nibh. Aenean justo diam, commodo vel felis eu, malesuada sodales purus. Nunc sollicitudin sed justo in eleifend. Fusce dictum ornare ligula, eu porttitor elit ullamcorper non. Aliquam erat volutpat. Mauris malesuada turpis non metus scelerisque tempus. Morbi dui turpis, mollis a ultrices blandit, commodo a enim. Mauris sit amet eleifend sapien.</p>
  <div class="foot"><span>Copyright © 2020 Terravane | All rights reserved</span></div>
</div>

<div class="slide c2" style="top:731px">
  <div class="ph" role="img" aria-label="Photo of a young activist in a yellow raincoat holding a save our planet placard" style="left:0;top:0;width:146px;height:210px;background:linear-gradient(160deg,#a9a59c 0%,#b79a3b 55%,#e0b822 100%)"></div>
  <span class="brand" style="top:9px"><i></i>TERRAVANE</span>
  <div style="position:absolute;left:120px;top:28px;width:182px;height:28px;background:var(--navy);border-bottom:2px solid var(--orange);color:var(--yellow);font-weight:700;font-size:8px;display:flex;align-items:center;justify-content:center">LOREM IPSUM CONSECTETUR</div>
  <p class="tiny" style="position:absolute;left:182px;top:82px;width:180px;color:#555;text-align:justify">Business valuation is a process and a set of procedures used to estimate the economic value of an owner's interest in a business. Valuation is used by financial market participants to determine the price they are willing to pay or receive to effect a sale of a business.</p>
  <svg style="position:absolute;left:182px;top:131px" width="10" height="10" viewBox="0 0 10 10"><rect x="1.5" y="1" width="7" height="8" fill="none" stroke="var(--navy)" stroke-width="1"/><path d="M3 4h4M3 6h3" stroke="var(--navy)" stroke-width=".8"/></svg>
  <svg style="position:absolute;left:278px;top:131px" width="10" height="10" viewBox="0 0 10 10"><path d="M1 5l8-4-3 8-1.5-3z" fill="var(--navy)"/></svg>
  <div style="position:absolute;left:182px;top:150px;font-size:5px;font-weight:600;color:var(--orange)">Your Contents Here</div>
  <div style="position:absolute;left:278px;top:150px;font-size:5px;font-weight:600;color:var(--orange)">Your Contents Here</div>
  <p class="tiny" style="position:absolute;left:182px;top:160px;width:85px;color:#555">Lorem ipsum dolor sit amet, consectetur adipiscing elit, sed do eiusmod tempor incididunt.</p>
  <p class="tiny" style="position:absolute;left:278px;top:160px;width:85px;color:#555">Lorem ipsum dolor sit amet, consectetur adipiscing elit, sed do eiusmod tempor incididunt.</p>
  <div class="foot"><span>Copyright © 2020 Terravane | All rights reserved</span></div>
</div>

<div class="slide c3" style="top:731px">
  <div class="bar"><div class="bar-title">TWO BULLET POINTS<small>HERE ADD YOUR TITLE</small></div></div><span class="brand"><i></i>TERRAVANE</span>
  <div class="pill" style="left:38px;top:85px;width:138px;height:66px">Lorem Ipsum is simply dummy unknown printer took a galley of type and scrambled it to make.</div>
  <div class="pill" style="left:212px;top:85px;width:138px;height:66px">Lorem Ipsum is simply dummy unknown printer took a galley of type and scrambled it to make.</div>
  <div class="foot"><span>Copyright © 2020 Terravane | All rights reserved</span></div>
</div>

<!-- row 3 -->
<div class="slide c1" style="top:966px">
  <div class="bar"><div class="bar-title">FOUR BULLET POINTS AND PICTURE<small>HERE ADD YOUR TITLE</small></div></div><span class="brand"><i></i>TERRAVANE</span>
  <div class="ph" role="img" aria-label="Illustration of two green trees on a grassy mound" style="left:22px;top:66px;width:145px;height:90px;border-radius:40px 40px 6px 6px;background:linear-gradient(180deg,#8ccb4a,#4ea43a)"></div>
  <div style="position:absolute;left:226px;top:55px;display:flex;flex-direction:column;gap:14px">
    <div style="display:flex;gap:10px"><div class="icon-dot"></div><div><div class="h6" style="font-size:4.6px">Your Text Here</div><p class="tiny" style="width:95px">Lorem ipsum dolor sit amet, nec an dicta equidem appellantur, ut has commune accommodare.</p></div></div>
    <div style="display:flex;gap:10px"><div class="icon-dot"></div><div><div class="h6" style="font-size:4.6px">Your Text Here</div><p class="tiny" style="width:95px">Lorem ipsum dolor sit amet, nec an dicta equidem appellantur, ut has commune accommodare.</p></div></div>
    <div style="display:flex;gap:10px"><div class="icon-dot"></div><div><div class="h6" style="font-size:4.6px">Your Text Here</div><p class="tiny" style="width:95px">Lorem ipsum dolor sit amet, nec an dicta equidem appellantur, ut has commune accommodare.</p></div></div>
    <div style="display:flex;gap:10px"><div class="icon-dot"></div><div><div class="h6" style="font-size:4.6px">Your Text Here</div><p class="tiny" style="width:95px">Lorem ipsum dolor sit amet, nec an dicta equidem appellantur, ut has commune accommodare.</p></div></div>
  </div>
  <div class="foot"><span>Copyright © 2020 Terravane | All rights reserved</span></div>
</div>

<div class="slide c2" style="top:966px">
  <div class="bar"><div class="bar-title">ADD YOUR AWESOME TITLE HERE<small>HERE ADD YOUR TITLE</small></div></div><span class="brand"><i></i>TERRAVANE</span>
  <div class="ph" role="img" aria-label="Illustration of a slender green tree" style="left:150px;top:68px;width:80px;height:140px;border-radius:40px 40px 4px 4px;background:linear-gradient(180deg,#9bd34e,#5aa93a 70%,#b07a3a)"></div>
  <div style="position:absolute;left:18px;top:52px;display:flex;flex-direction:column;gap:10px">
    <div style="display:flex;gap:8px"><div class="num" style="background:var(--green)">1</div><div><div class="h6" style="font-size:4.4px">Contents Title</div><p class="tiny" style="width:82px">Lorem ipsum randomised words which in some form, by injected humour.</p></div></div>
    <div style="display:flex;gap:8px"><div class="num" style="background:var(--green)">2</div><div><div class="h6" style="font-size:4.4px">Contents Title</div><p class="tiny" style="width:82px">Lorem ipsum randomised words which in some form, by injected humour.</p></div></div>
    <div style="display:flex;gap:8px"><div class="num" style="background:var(--green)">3</div><div><div class="h6" style="font-size:4.4px">Contents Title</div><p class="tiny" style="width:82px">Lorem ipsum randomised words which in some form, by injected humour.</p></div></div>
    <div style="display:flex;gap:8px"><div class="num" style="background:var(--green)">4</div><div><div class="h6" style="font-size:4.4px">Contents Title</div><p class="tiny" style="width:82px">Lorem ipsum randomised words which in some form, by injected humour.</p></div></div>
  </div>
  <div style="position:absolute;left:252px;top:52px;display:flex;flex-direction:column;gap:10px">
    <div style="display:flex;gap:8px"><div class="num" style="background:#8d9096">1</div><div><div class="h6" style="font-size:4.4px">Contents Title</div><p class="tiny" style="width:82px">Lorem ipsum randomised words which in some form, by injected humour.</p></div></div>
    <div style="display:flex;gap:8px"><div class="num" style="background:#8d9096">2</div><div><div class="h6" style="font-size:4.4px">Contents Title</div><p class="tiny" style="width:82px">Lorem ipsum randomised words which in some form, by injected humour.</p></div></div>
    <div style="display:flex;gap:8px"><div class="num" style="background:#8d9096">3</div><div><div class="h6" style="font-size:4.4px">Contents Title</div><p class="tiny" style="width:82px">Lorem ipsum randomised words which in some form, by injected humour.</p></div></div>
    <div style="display:flex;gap:8px"><div class="num" style="background:#8d9096">4</div><div><div class="h6" style="font-size:4.4px">Contents Title</div><p class="tiny" style="width:82px">Lorem ipsum randomised words which in some form, by injected humour.</p></div></div>
  </div>
  <div class="foot"><span>Copyright © 2020 Terravane | All rights reserved</span></div>
</div>

<div class="slide c3" style="top:966px">
  <div class="bar"><div class="bar-title">SIX POINTS<small>HERE ADD YOUR TITLE</small></div></div><span class="brand"><i></i>TERRAVANE</span>
  <div style="position:absolute;left:22px;top:75px;display:grid;grid-template-columns:120px 120px 120px;row-gap:28px">
    <div style="display:flex;gap:6px"><div class="num" style="background:var(--green)">01</div><div><div class="h6" style="font-size:4.6px">Project name</div><p class="tiny" style="width:82px">Lorem ipsum is simply dummy unknown printer took a galley of type.</p></div></div>
    <div style="display:flex;gap:6px"><div class="num" style="background:var(--green)">02</div><div><div class="h6" style="font-size:4.6px">Project name</div><p class="tiny" style="width:82px">Lorem ipsum is simply dummy unknown printer took a galley of type.</p></div></div>
    <div style="display:flex;gap:6px"><div class="num" style="background:var(--green)">03</div><div><div class="h6" style="font-size:4.6px">Project name</div><p class="tiny" style="width:82px">Lorem ipsum is simply dummy unknown printer took a galley of type.</p></div></div>
    <div style="display:flex;gap:6px"><div class="num" style="background:var(--green)">04</div><div><div class="h6" style="font-size:4.6px">Project name</div><p class="tiny" style="width:82px">Lorem ipsum is simply dummy unknown printer took a galley of type.</p></div></div>
    <div style="display:flex;gap:6px"><div class="num" style="background:var(--green)">05</div><div><div class="h6" style="font-size:4.6px">Project name</div><p class="tiny" style="width:82px">Lorem ipsum is simply dummy unknown printer took a galley of type.</p></div></div>
    <div style="display:flex;gap:6px"><div class="num" style="background:var(--green)">06</div><div><div class="h6" style="font-size:4.6px">Project name</div><p class="tiny" style="width:82px">Lorem ipsum is simply dummy unknown printer took a galley of type.</p></div></div>
  </div>
  <div class="foot"><span>Copyright © 2020 Terravane | All rights reserved</span></div>
</div>

<!-- row 4 -->
<div class="slide c1" style="top:1202px">
  <div style="position:absolute;left:44px;top:34px;width:40px;height:1.5px;background:var(--navy)"></div>
  <p style="position:absolute;left:44px;top:38px;width:145px;font-weight:600;font-size:8px;color:var(--navy);line-height:1.3">Success is not only what you achieve in your life, but also what you inspire in the lives of others</p>
  <div style="position:absolute;left:0;top:110px;width:387px;height:107px;background:var(--navy)"></div>
  <div style="position:absolute;left:36px;top:140px;display:flex;gap:20px;color:#fff">
    <div style="width:95px"><b style="font-size:6px;font-weight:600">Lorem ipsum dolor</b><p class="tiny" style="color:#dfe4ec;font-size:4.6px;margin-top:8px">Lorem ipsum dolor sit amet, consectetur adipiscing elit, sed do eiusmod tempor</p></div>
    <div style="width:95px"><b style="font-size:6px;font-weight:600">Lorem ipsum dolor</b><p class="tiny" style="color:#dfe4ec;font-size:4.6px;margin-top:8px">Lorem ipsum dolor sit amet, consectetur adipiscing elit, sed do eiusmod tempor</p></div>
    <div style="width:95px"><b style="font-size:6px;font-weight:600">Lorem ipsum dolor</b><p class="tiny" style="color:#dfe4ec;font-size:4.6px;margin-top:8px">Lorem ipsum dolor sit amet, consectetur adipiscing elit, sed do eiusmod tempor</p></div>
  </div>
</div>

<div class="slide c2" style="top:1202px">
  <div class="bar"><div class="bar-title">INFOGRAPHIC<small>HERE ADD YOUR TITLE</small></div></div><span class="brand"><i></i>TERRAVANE</span>
  <svg style="position:absolute;left:135px;top:66px" width="115" height="115" viewBox="0 0 115 115"><circle cx="57.5" cy="57.5" r="54" fill="none" stroke="#cfd8e3" stroke-width=".8" stroke-dasharray="2 2"/><circle cx="57.5" cy="57.5" r="42" fill="var(--navy)"/><g fill="#fff" stroke-width="1.3"><circle cx="12" cy="22" r="3" stroke="var(--orange)"/><circle cx="4" cy="57" r="3" stroke="var(--orange)"/><circle cx="12" cy="92" r="3" stroke="var(--blue)"/><circle cx="103" cy="22" r="3" stroke="var(--blue)"/><circle cx="111" cy="57" r="3" stroke="var(--green)"/><circle cx="103" cy="92" r="3" stroke="var(--orange)"/></g></svg>
  <div style="position:absolute;left:163px;top:112px;width:60px;text-align:center;color:#fff;font-weight:700;font-size:6px;line-height:1.25">Add Your Awesome Title Here</div>
  <div class="info-box" style="left:62px;top:80px;background:var(--orange)">Composition of the board</div>
  <div class="info-box" style="left:56px;top:113px;background:var(--green)">Clarity of roles &amp; responsibilities</div>
  <div class="info-box" style="left:62px;top:146px;background:var(--blue)">Joint vision</div>
  <div class="info-box" style="left:260px;top:80px;background:var(--blue)">Ability to use the strengths of all members</div>
  <div class="info-box" style="left:265px;top:113px;background:var(--green)">Ability to resolve conflicts between the board &amp; staff</div>
  <div class="info-box" style="left:260px;top:146px;background:var(--orange)">Structure &amp; organisation of the work</div>
  <div class="foot"><span>Copyright © 2020 Terravane | All rights reserved</span></div>
</div>

<div class="slide c3" style="top:1202px">
  <div class="bar"><div class="bar-title">ADD YOUR AWESOME TITLE HERE<small>HERE ADD YOUR TITLE</small></div></div><span class="brand"><i></i>TERRAVANE</span>
  <div class="card" style="left:48px;background:linear-gradient(180deg,var(--yellow),var(--orange))"><div class="disc"><svg width="22" height="14" viewBox="0 0 22 14"><circle cx="5" cy="9" r="4" fill="none" stroke="var(--navy)" stroke-width="1.3"/><circle cx="17" cy="9" r="4" fill="none" stroke="var(--navy)" stroke-width="1.3"/><path d="M5 9l4-6h6l2 6M9 3l3 6" fill="none" stroke="var(--navy)" stroke-width="1.3"/></svg></div><b>Your Contents Here</b><p>Lorem ipsum dolor sit amet, consectetur adipiscing elit, sed do eiusmod tempor incididunt.</p></div>
  <div class="card" style="left:149px;background:linear-gradient(180deg,var(--lime),var(--green))"><div class="disc"><svg width="16" height="16" viewBox="0 0 16 16"><path d="M8 2l5 9H3z" fill="none" stroke="var(--green)" stroke-width="1.8"/></svg></div><b>Your Contents Here</b><p>Lorem ipsum dolor sit amet, consectetur adipiscing elit, sed do eiusmod tempor incididunt.</p></div>
  <div class="card" style="left:250px;background:linear-gradient(180deg,var(--sky),var(--blue))"><div class="disc"><svg width="18" height="18" viewBox="0 0 18 18"><circle cx="9" cy="9" r="7" fill="var(--blue)"/><path d="M4 7c3 1 4-2 6 0s3 3 4 1" fill="none" stroke="var(--green)" stroke-width="2"/></svg></div><b>Your Contents Here</b><p>Lorem ipsum dolor sit amet, consectetur adipiscing elit, sed do eiusmod tempor incididunt.</p></div>
  <div class="foot"><span>Copyright © 2020 Terravane | All rights reserved</span></div>
</div>

<!-- row 5 -->
<div class="slide c1" style="top:1432px">
  <div class="bar"><div class="bar-title">TIMELINE<small>HERE ADD YOUR TITLE</small></div></div><span class="brand"><i></i>TERRAVANE</span>
  <svg style="position:absolute;left:0;top:80px" width="387" height="30" viewBox="0 0 387 30">
    <line x1="22" y1="18" x2="365" y2="18" stroke="#dfe3e8" stroke-width="1"/>
    <g font-family="Montserrat,sans-serif" font-size="6" font-weight="700" fill="var(--navy)" text-anchor="middle"><text x="38" y="8">2015</text><text x="100" y="8">2016</text><text x="162" y="8">2017</text><text x="224" y="8">2018</text><text x="286" y="8">2019</text><text x="348" y="8">2020</text></g>
    <circle cx="38" cy="18" r="4" fill="var(--green)"/><circle cx="100" cy="18" r="4" fill="var(--blue)"/><circle cx="162" cy="18" r="4" fill="var(--yellow)"/><circle cx="224" cy="18" r="4" fill="var(--green)"/><circle cx="286" cy="18" r="4" fill="var(--blue)"/><circle cx="348" cy="18" r="4" fill="var(--yellow)"/>
  </svg>
  <div style="position:absolute;left:16px;top:125px;display:flex;gap:6px;text-align:center">
    <div style="width:56px"><div class="h6" style="font-size:4.4px">Project name</div><p class="tiny">Lorem ipsum is simply dummy unknown printer took a galley of type.</p></div>
    <div style="width:56px"><div class="h6" style="font-size:4.4px">Project name</div><p class="tiny">Lorem ipsum is simply dummy unknown printer took a galley of type.</p></div>
    <div style="width:56px"><div class="h6" style="font-size:4.4px">Project name</div><p class="tiny">Lorem ipsum is simply dummy unknown printer took a galley of type.</p></div>
    <div style="width:56px"><div class="h6" style="font-size:4.4px">Project name</div><p class="tiny">Lorem ipsum is simply dummy unknown printer took a galley of type.</p></div>
    <div style="width:56px"><div class="h6" style="font-size:4.4px">Project name</div><p class="tiny">Lorem ipsum is simply dummy unknown printer took a galley of type.</p></div>
    <div style="width:56px"><div class="h6" style="font-size:4.4px">Project name</div><p class="tiny">Lorem ipsum is simply dummy unknown printer took a galley of type.</p></div>
  </div>
  <div class="foot"><span>Copyright © 2020 Terravane | All rights reserved</span></div>
</div>

<div class="slide c2" style="top:1432px">
  <span class="brand"><i></i>TERRAVANE</span>
  <div class="ph" role="img" aria-label="Navy world map with highlighted regions" style="left:75px;top:8px;width:305px;height:190px;border-radius:40%;background:radial-gradient(ellipse at 50% 50%,#2a4268 0%,#1f3558 60%,rgba(31,53,88,0) 72%)"></div>
  <div style="position:absolute;left:24px;top:135px;font-weight:500;font-size:11px;color:var(--navy);line-height:1.3">Add Your<br>Awesome<br>Title Here</div>
  <div class="foot"><span>Copyright © 2020 Terravane | All rights reserved</span></div>
</div>

<div class="slide c3" style="top:1432px">
  <span class="brand"><i></i>TERRAVANE</span>
  <div style="position:absolute;left:0;width:100%;top:12px;text-align:center;font-size:11px;font-weight:500;color:var(--navy)">OUR TEAM</div>
  <div style="position:absolute;left:0;width:100%;top:26px;text-align:center;font-size:4px;font-weight:800;letter-spacing:1px;color:var(--blue)">HERE ADD YOUR TITLE</div>
  <div class="team-card" style="left:14px"><div class="avatar" role="img" aria-label="Team member portrait"></div><b>Your Name</b><span>Founder</span><p class="tiny">Lorem ipsum dolor sit amet, consectetur adipiscing elit. Donec mauris lorem, vestibulum ac rutrum id.</p><div class="line"></div></div>
  <div class="team-card" style="left:98px;background:#f3f4f6;padding:6px"><div class="avatar" role="img" aria-label="Team member portrait"></div><b>Your Name</b><span>Global Account Executive</span><p class="tiny">Lorem ipsum dolor sit amet, consectetur adipiscing elit. Donec mauris lorem, vestibulum ac rutrum id.</p><div class="line"></div></div>
  <div class="team-card" style="left:196px"><div class="avatar" role="img" aria-label="Team member portrait"></div><b>Your Name</b><span>Founder</span><p class="tiny">Lorem ipsum dolor sit amet, consectetur adipiscing elit. Donec mauris lorem, vestibulum ac rutrum id.</p><div class="line"></div></div>
  <div class="team-card" style="left:286px;background:#f3f4f6;padding:6px"><div class="avatar" role="img" aria-label="Team member portrait"></div><b>Your Name</b><span>Global Account Executive</span><p class="tiny">Lorem ipsum dolor sit amet, consectetur adipiscing elit. Donec mauris lorem, vestibulum ac rutrum id.</p><div class="line"></div></div>
  <div class="foot"><span>Copyright © 2020 Terravane | All rights reserved</span></div>
</div>

<!-- row 6 -->
<div class="slide c1" style="top:1663px">
  <div class="bar"><div class="bar-title">YOUR AWESOME TEXT HERE<small>HERE ADD YOUR TITLE</small></div></div><span class="brand"><i></i>TERRAVANE</span>
  <div style="position:absolute;left:30px;top:60px;display:flex;flex-direction:column;gap:14px">
    <div style="display:flex;gap:10px"><div class="label" style="background:var(--orange)">Business valuation</div><p class="tiny" style="width:262px;color:#555">Lorem ipsum dolor sit amet, consectetur adipiscing elit, sed do eiusmod tempor incididunt ut labore et dolore magna aliqua. Ut enim ad minim veniam, quis nostrud exercitation.</p></div>
    <div style="display:flex;gap:10px"><div class="label" style="background:var(--green)">Business valuation</div><p class="tiny" style="width:262px;color:#555">Lorem ipsum dolor sit amet, consectetur adipiscing elit, sed do eiusmod tempor incididunt ut labore et dolore magna aliqua. Ut enim ad minim veniam, quis nostrud exercitation.</p></div>
    <div style="display:flex;gap:10px"><div class="label" style="background:var(--orange)">Business valuation</div><p class="tiny" style="width:262px;color:#555">Lorem ipsum dolor sit amet, consectetur adipiscing elit, sed do eiusmod tempor incididunt ut labore et dolore magna aliqua. Ut enim ad minim veniam, quis nostrud exercitation.</p></div>
    <div style="display:flex;gap:10px"><div class="label" style="background:var(--green)">Business valuation</div><p class="tiny" style="width:262px;color:#555">Lorem ipsum dolor sit amet, consectetur adipiscing elit, sed do eiusmod tempor incididunt ut labore et dolore magna aliqua. Ut enim ad minim veniam, quis nostrud exercitation.</p></div>
  </div>
  <div class="foot"><span>Copyright © 2020 Terravane | All rights reserved</span></div>
</div>

<div class="slide c2" style="top:1663px">
  <div class="bar"><div class="bar-title">ADD YOUR AWESOME TITLE HERE<small>HERE ADD YOUR TITLE</small></div></div><span class="brand"><i></i>TERRAVANE</span>
  <div style="position:absolute;left:28px;top:48px;display:flex;gap:22px">
    <div style="width:96px"><div class="h6" style="font-size:4.8px">Lorem ipsum</div><p class="tiny" style="margin-top:3px">• Lorem ipsum dolor sit amet, consectetur adipiscing elit.<br>• Lorem ipsum dolor sit amet, consectetur adipiscing elit. Mauris porttitor congue massa.</p></div>
    <div style="width:96px"><div class="h6" style="font-size:4.8px">Lorem ipsum</div><p class="tiny" style="margin-top:3px">• Lorem ipsum dolor sit amet, consectetur adipiscing elit.<br>• Lorem ipsum dolor sit amet, consectetur adipiscing elit. Mauris porttitor congue massa.</p></div>
    <div style="width:96px"><div class="h6" style="font-size:4.8px">Lorem ipsum</div><p class="tiny" style="margin-top:3px">• Lorem ipsum dolor sit amet, consectetur adipiscing elit.<br>• Lorem ipsum dolor sit amet, consectetur adipiscing elit. Mauris porttitor congue massa.</p></div>
  </div>
  <table class="grid-table" style="left:16px;top:104px;width:355px">
    <tr><th>Text</th><th>Text</th><th>Text</th><th>Text</th><th style="background:var(--navy);color:#fff">TERRAVANE</th><th>Text</th></tr>
    <tr><td>Data</td><td>Data</td><td>Data</td><td>Data</td><td>Data</td><td>Data</td></tr>
    <tr><td>Data</td><td>Data</td><td>Data</td><td>Data</td><td>Data</td><td>Data</td></tr>
    <tr><td>Data</td><td>Data</td><td>Data</td><td>Data</td><td>Data</td><td>Data</td></tr>
    <tr><td>Data</td><td>Data</td><td>Data</td><td>Data</td><td>Data</td><td>Data</td></tr>
    <tr><td>Data</td><td>Data</td><td>Data</td><td>Data</td><td>Data</td><td>Data</td></tr>
  </table>
  <div class="foot"><span>Copyright © 2020 Terravane | All rights reserved</span></div>
</div>

<div class="slide c3" style="top:1663px">
  <div class="bar"><div class="bar-title">STATISTIC<small>HERE ADD YOUR TITLE</small></div></div><span class="brand"><i></i>TERRAVANE</span>
  <div style="position:absolute;left:0;width:100%;top:46px;text-align:center;font-weight:500;font-size:13px;color:var(--navy)">Your awesome text here</div>
  <p class="tiny" style="position:absolute;left:78px;top:64px;width:232px;text-align:center">Lorem Ipsum the printing and typesetting industry. Lorem Ipsum has been the industry's standard dummy text ever since the 1500s, when an unknown printer took a galley of type and scrambled it to make a type specimen book. It has survived not only five centuries.</p>
  <svg style="position:absolute;left:78px;top:102px" width="235" height="50" viewBox="0 0 235 50">
    <g fill="none" stroke-width="3"><circle cx="30" cy="25" r="19" stroke="#e8ebef"/><circle cx="112" cy="25" r="19" stroke="#e8ebef"/><circle cx="194" cy="25" r="19" stroke="#e8ebef"/>
    <circle cx="30" cy="25" r="19" stroke="var(--green)" stroke-dasharray="59.7 119.4" transform="rotate(-90 30 25)"/>
    <circle cx="112" cy="25" r="19" stroke="var(--blue)" stroke-dasharray="89.5 119.4" transform="rotate(-90 112 25)"/>
    <circle cx="194" cy="25" r="19" stroke="var(--orange)" stroke-dasharray="47.8 119.4" transform="rotate(-90 194 25)"/></g>
    <g font-family="Montserrat,sans-serif" font-size="9" font-weight="600" fill="var(--navy)" text-anchor="middle"><text x="30" y="28">50%</text><text x="112" y="28">75%</text><text x="194" y="28">40%</text></g>
  </svg>
  <div style="position:absolute;left:82px;top:168px;display:flex;gap:30px">
    <p class="tiny" style="width:52px;text-align:center">Lorem ipsum dolor amet consectetur dolor</p>
    <p class="tiny" style="width:52px;text-align:center">Lorem ipsum dolor amet consectetur dolor</p>
    <p class="tiny" style="width:52px;text-align:center">Lorem ipsum dolor amet consectetur dolor</p>
  </div>
  <div class="foot"><span>Copyright © 2020 Terravane | All rights reserved</span></div>
</div>

<!-- row 7 -->
<div class="slide c1" style="top:1893px">
  <div class="bar"><div class="bar-title">STATISTIC AND TEXT<small>HERE ADD YOUR TITLE</small></div></div><span class="brand"><i></i>TERRAVANE</span>
  <svg style="position:absolute;left:14px;top:44px" width="230" height="145" viewBox="0 0 230 145">
    <g stroke="#eceef1" stroke-width=".5"><line x1="20" y1="10" x2="225" y2="10"/><line x1="20" y1="27" x2="225" y2="27"/><line x1="20" y1="44" x2="225" y2="44"/><line x1="20" y1="61" x2="225" y2="61"/><line x1="20" y1="78" x2="225" y2="78"/><line x1="20" y1="95" x2="225" y2="95"/><line x1="20" y1="112" x2="225" y2="112"/></g>
    <g font-family="Poppins,sans-serif" font-size="3.6" fill="#777"><text x="12" y="12">6</text><text x="12" y="29">5</text><text x="12" y="46">4</text><text x="12" y="63">3</text><text x="12" y="80">2</text><text x="12" y="97">1</text><text x="12" y="114">0</text>
    <text x="36" y="122">Category 1</text><text x="86" y="122">Category 2</text><text x="136" y="122">Category 3</text><text x="186" y="122">Category 4</text>
    <text x="88" y="138">■ Series 1  ■ Series 2  ■ Series 3</text></g>
    <rect x="38" y="38" width="7" height="74" fill="var(--green)"/><rect x="48" y="70" width="7" height="42" fill="var(--blue)"/><rect x="58" y="78" width="7" height="34" fill="var(--yellow)"/>
    <rect x="88" y="36" width="7" height="76" fill="var(--blue)"/><rect x="98" y="78" width="7" height="34" fill="var(--green)"/><rect x="108" y="78" width="7" height="34" fill="var(--yellow)"/>
    <rect x="138" y="53" width="7" height="59" fill="var(--green)"/><rect x="148" y="75" width="7" height="37" fill="var(--blue)"/><rect x="158" y="61" width="7" height="51" fill="var(--yellow)"/>
    <rect x="188" y="32" width="7" height="80" fill="var(--green)"/><rect x="198" y="44" width="7" height="68" fill="var(--blue)"/><rect x="208" y="27" width="7" height="85" fill="var(--yellow)"/>
  </svg>
  <div style="position:absolute;left:255px;top:36px;width:132px;height:156px;background:#f3f4f6"></div>
  <div style="position:absolute;left:268px;top:52px;display:flex;flex-direction:column;gap:12px">
    <div style="display:flex;gap:6px"><div class="icon-dot" style="width:20px;height:20px"></div><div><div style="font-size:5.5px;color:var(--navy)">Project name</div><p class="tiny" style="width:82px">Lorem ipsum dolor sit amet, nec an dicta equidem appellantur, ut has commune.</p></div></div>
    <div style="display:flex;gap:6px"><div class="icon-dot" style="width:20px;height:20px"></div><div><div style="font-size:5.5px;color:var(--navy)">Project name</div><p class="tiny" style="width:82px">Lorem ipsum dolor sit amet, nec an dicta equidem appellantur, ut has commune.</p></div></div>
    <div style="display:flex;gap:6px"><div class="icon-dot" style="width:20px;height:20px"></div><div><div style="font-size:5.5px;color:var(--navy)">Project name</div><p class="tiny" style="width:82px">Lorem ipsum dolor sit amet, nec an dicta equidem appellantur, ut has commune.</p></div></div>
  </div>
  <div class="foot"><span>Copyright © 2020 Terravane | All rights reserved</span></div>
</div>

<div class="slide c2" style="top:1893px">
  <span class="brand"><i></i>TERRAVANE</span>
  <div style="position:absolute;left:26px;top:52px;font-weight:500;font-size:11px;color:var(--navy)">STEPS TO SUCCESS</div>
  <div style="position:absolute;left:52px;top:66px;font-size:4px;color:#aaa">Write here a great subtitle</div>
  <div class="ph" role="img" aria-label="Green figure stepping up a staircase" style="left:200px;top:8px;width:40px;height:82px;border-radius:20px 20px 4px 4px;background:linear-gradient(180deg,#8ccb4a,#4ea43a)"></div>
  <div class="step" style="left:22px;top:150px">01</div>
  <div class="step" style="left:94px;top:126px">02</div>
  <div class="step" style="left:166px;top:103px">03</div>
  <div class="step" style="left:235px;top:79px">04</div>
  <div class="step" style="left:304px;top:55px">05</div>
  <div style="position:absolute;left:22px;top:163px;width:64px"><div class="h6" style="font-size:4.2px">Lorem ipsum dolor</div><p class="tiny">Lorem ipsum dolor sit amet, consectetur adipiscing elit.</p></div>
  <div style="position:absolute;left:94px;top:139px;width:64px"><div class="h6" style="font-size:4.2px">Lorem ipsum dolor</div><p class="tiny">Lorem ipsum dolor sit amet, consectetur adipiscing elit.</p></div>
  <div style="position:absolute;left:166px;top:116px;width:64px"><div class="h6" style="font-size:4.2px">Lorem ipsum dolor</div><p class="tiny">Lorem ipsum dolor sit amet, consectetur adipiscing elit.</p></div>
  <div style="position:absolute;left:235px;top:92px;width:64px"><div class="h6" style="font-size:4.2px">Lorem ipsum dolor</div><p class="tiny">Lorem ipsum dolor sit amet, consectetur adipiscing elit.</p></div>
  <div style="position:absolute;left:304px;top:68px;width:64px"><div class="h6" style="font-size:4.2px">Lorem ipsum dolor</div><p class="tiny">Lorem ipsum dolor sit amet, consectetur adipiscing elit.</p></div>
  <div class="foot"><span>Copyright © 2020 Terravane | All rights reserved</span></div>
</div>

<div class="slide c3" style="top:1893px">
  <div class="bar"><div class="bar-title">ADD YOUR AWESOME TITLE HERE<small>HERE ADD YOUR TITLE</small></div></div><span class="brand"><i></i>TERRAVANE</span>
  <div style="position:absolute;left:36px;top:62px;width:318px;display:grid;grid-template-columns:repeat(4,1fr);gap:1px;background:#e3e6ea">
    <div style="background:var(--navy);color:#fff;font-size:4.6px;font-weight:700;height:18px;display:flex;align-items:center;padding-left:5px">ADD YOUR TITLE</div>
    <div style="background:var(--navy);color:#fff;font-size:4.6px;font-weight:700;height:18px;display:flex;align-items:center;padding-left:5px">ADD YOUR TITLE</div>
    <div style="background:#fff;color:var(--navy);font-size:4.6px;font-weight:700;height:18px;display:flex;align-items:center;padding-left:5px;gap:3px"><i style="width:6px;height:6px;border-radius:50%;background:var(--green);display:block"></i>TERRAVANE</div>
    <div style="background:var(--navy);color:#fff;font-size:4.6px;font-weight:700;height:18px;display:flex;align-items:center;padding-left:5px">ADD YOUR TITLE</div>
    <div style="background:#f5f6f8;padding:6px 5px;height:41px"><div class="h6" style="font-size:4px">Project name</div><p class="tiny">Lorem ipsum is simply dummy unknown printer took a galley of type.</p></div>
    <div style="background:#f5f6f8;padding:6px 5px"><div class="h6" style="font-size:4px">Project name</div><p class="tiny">Lorem ipsum is simply dummy unknown printer took a galley of type.</p></div>
    <div style="background:#e9ecef;padding:6px 5px"><div class="h6" style="font-size:4px">Project name</div><p class="tiny">Lorem ipsum is simply dummy unknown printer took a galley of type.</p></div>
    <div style="background:#f5f6f8;padding:6px 5px"><div class="h6" style="font-size:4px">Project name</div><p class="tiny">Lorem ipsum is simply dummy unknown printer took a galley of type.</p></div>
    <div style="background:#f5f6f8;padding:6px 5px;height:41px"><div class="h6" style="font-size:4px">Project name</div><p class="tiny">Lorem ipsum is simply dummy unknown printer took a galley of type.</p></div>
    <div style="background:#f5f6f8;padding:6px 5px"><div class="h6" style="font-size:4px">Project name</div><p class="tiny">Lorem ipsum is simply dummy unknown printer took a galley of type.</p></div>
    <div style="background:#e9ecef;padding:6px 5px"><div class="h6" style="font-size:4px">Project name</div><p class="tiny">Lorem ipsum is simply dummy unknown printer took a galley of type.</p></div>
    <div style="background:#f5f6f8;padding:6px 5px"><div class="h6" style="font-size:4px">Project name</div><p class="tiny">Lorem ipsum is simply dummy unknown printer took a galley of type.</p></div>
  </div>
  <div class="foot"><span>Copyright © 2020 Terravane | All rights reserved</span></div>
</div>

<!-- row 8 -->
<div class="slide c1" style="top:2123px">
  <div class="ph" role="img" aria-label="Photo of wind turbines against a sunset sky" style="inset:0;background:linear-gradient(180deg,#2c4266 0%,#4f5d72 45%,#b07a48 70%,#3e3428 100%)"></div>
  <div class="overlay-title" style="left:68px;top:104px;font-size:9.5px">Why we need to do a climate risk assessment</div>
  <div style="position:absolute;left:68px;top:118px;width:270px;height:1px;background:var(--orange)"></div>
</div>

<div class="slide c2" style="top:2123px">
  <div class="ph" role="img" aria-label="Photo of climate protest crowd with a planet placard under a navy overlay" style="inset:0;background:linear-gradient(100deg,#233a5f 0%,#2f4a70 55%,#5b6f86 100%)"></div>
  <div class="overlay-title" style="left:73px;top:76px;font-size:17px;line-height:1.25">Why we need<br>to do a climate<br>risk assessment</div>
</div>

<div class="slide c3" style="top:2123px">
  <div class="ph" role="img" aria-label="Illustration of a light bulb with a green sprout" style="left:25px;top:0;width:88px;height:165px;border-radius:0 0 44px 44px;background:linear-gradient(180deg,#5aa93a 0%,#9bd34e 40%,#fece3e 70%,#f6a01a 100%)"></div>
  <div style="position:absolute;left:210px;top:28px;display:flex;gap:22px;font-family:Poppins,sans-serif;font-size:3.4px;color:#666;text-align:center">
    <div><svg width="7" height="7" viewBox="0 0 7 7"><circle cx="3.5" cy="3.5" r="3" fill="var(--navy)"/></svg><br>Social Media<br>@terravane</div>
    <div><svg width="8" height="6" viewBox="0 0 8 6"><rect x=".5" y=".5" width="7" height="5" fill="none" stroke="var(--navy)"/><path d="M.5 .5l3.5 3 3.5-3" fill="none" stroke="var(--navy)"/></svg><br>Email<br>info@terravane.co</div>
    <div><svg width="7" height="7" viewBox="0 0 7 7"><path d="M1 1c0 3 2 5 5 5l.5-1.5-1.5-1-1 .8c-.8-.4-1.4-1-1.8-1.8l.8-1-1-1.5z" fill="var(--navy)"/></svg><br>Phone<br>+1 555 0142</div>
    <div><svg width="7" height="7" viewBox="0 0 7 7"><circle cx="3.5" cy="3.5" r="3" fill="none" stroke="var(--navy)"/><path d="M.5 3.5h6M3.5 .5v6" stroke="var(--navy)" stroke-width=".6"/></svg><br>Website<br>www.terravane.co</div>
  </div>
  <div class="cover-brand" style="position:absolute;left:250px;top:60px;font-size:9px"><i style="width:12px;height:12px"></i>TERRAVANE</div>
  <div style="position:absolute;left:100px;top:110px;font-weight:500;font-size:12.5px;line-height:1.15;color:var(--navy)">LINKING<br>SCIENCE AND<br>DECISION-MAKING</div>
  <div style="position:absolute;left:0;bottom:0;width:100%;height:5px;background:var(--navy)"></div>
</div>

<!-- row 9 -->
<div class="slide c2" style="top:2347px">
  <div class="bar"></div><span class="brand"><i></i>TERRAVANE</span>
  <div class="foot"><span>Copyright © 2020 Terravane | All rights reserved</span></div>
</div>

</body>
</html>
```